Mr Pellowes Yard Works flyer for newsletter

I need a professional looking flyer design for my company Mr Pellowes Yard Works based in New Braunfels, TX to boost sales. Must include the following: Lawn service starting at $40 (mowing, edging, leaf blowing) Tree trimming starting at $125. Other services-mulching, shrub trimming, aeration, flower bed maintenance, Fall/spring clean up. Serving New Braunfels and surrounding areas. To set up and estimate please call 512 555 0143 or email mrpellowesyard@example-mail.net

Industry/Entity Type

Landscaping

Font styles to use
Serif

Colors

Designer to choose colors to be used in the design.

Requirements
Must have
• Phone number 512 555 0143
• Email mrpellowesyard@example-mail.net

```html
<!DOCTYPE html>
<html lang="en">
<head>
<meta charset="utf-8">
<title>Mr Pellowes Yard Works – Flyer</title>
<link rel="stylesheet" href="https://fonts.googleapis.com/css2?family=Lato:wght@400;700;900&display=swap">
<style>
  :root {
    --forest: #0d6a2a;
    --lime: #d5e28b;
    --lime-soft: #e3ecab;
    --paper-grey: #e7e7e7;
    --price-red: #e8262a;
    --ink: #2a2a2a;
    --white: #ffffff;
    --backdrop: #ececec;
  }
  * { box-sizing: border-box; margin: 0; padding: 0; }
  html, body { width: 1195px; height: 1200px; overflow: hidden; }
  body {
    background: var(--backdrop);
    font-family: "Lato", Arial, sans-serif;
    position: relative;
  }
  .flyer {
    position: absolute;
    left: 197px; top: 35px;
    width: 800px; height: 1130px;
    background: var(--lime);
    overflow: hidden;
    box-shadow: 0 4px 18px rgba(0,0,0,.18);
  }
  .hero-art { position: absolute; left: 0; top: 0; width: 800px; height: 520px; }
  .area-band {
    position: absolute; right: 0; top: 0;
    width: 480px; height: 118px;
    padding: 24px 26px 0 0;
    text-align: right;
    color: var(--white);
    font-weight: 900; font-size: 29px; line-height: 1.2;
  }
  .brand-name {
    position: absolute; left: 430px; top: 262px; width: 360px;
    color: var(--forest);
    font-weight: 900; font-size: 70px; line-height: .92;
    text-align: center;
  }
  .offers { position: absolute; left: 40px; top: 530px; width: 450px; }
  .offer-title { color: var(--forest); font-weight: 900; font-size: 34px; line-height: 1.1; }
  .offer-line {
    color: var(--ink); font-size: 40px; line-height: 1;
    display: flex; align-items: baseline; gap: 8px;
  }
  .price { color: var(--price-red); font-weight: 900; font-size: 84px; line-height: .85; }
  .price small { font-size: 40px; vertical-align: 26px; }
  .offer-note { color: var(--ink); font-size: 23px; margin-top: 4px; }
  .offer + .offer { margin-top: 16px; }
  .extras { position: absolute; left: 500px; top: 575px; list-style: none; }
  .extras li {
    color: var(--forest); font-weight: 900; font-size: 23px;
    margin-bottom: 14px; display: flex; align-items: center; gap: 14px;
  }
  .extras li::before { content: ""; width: 9px; height: 9px; background: var(--price-red); }
  .contact-zone {
    position: absolute; left: 0; top: 805px; width: 800px; height: 325px;
    background: var(--paper-grey); border-top: 6px solid var(--forest);
  }
  .contact {
    position: absolute; left: 0; top: 22px; width: 800px;
    text-align: center; color: var(--ink); font-size: 29px; line-height: 1.3;
  }
  .contact .lead, .contact b { font-weight: 900; }
  .service-strip { position: absolute; left: 0; bottom: 0; width: 800px; height: 185px; }
</style>
</head>
<body>
  <main class="flyer">
    <svg class="hero-art" viewBox="0 0 800 520">
      <defs>
        <linearGradient id="mowerPhoto" x1="0" y1="0" x2="1" y2="1">
          <stop offset="0" stop-color="#3f7a2a"/>
          <stop offset=".55" stop-color="#4fa234"/>
          <stop offset="1" stop-color="#2f7d22"/>
        </linearGradient>
      </defs>
      <rect x="320" y="0" width="480" height="118" fill="var(--forest)"/>
      <rect x="330" y="130" width="470" height="14" fill="var(--forest)"/>
      <rect x="330" y="158" width="470" height="14" fill="var(--forest)"/>
      <rect x="330" y="186" width="470" height="18" fill="var(--forest)"/>
      <circle cx="190" cy="200" r="292" fill="var(--white)"/>
      <circle cx="190" cy="200" r="285" fill="var(--lime-soft)"/>
      <circle cx="190" cy="200" r="278" fill="url(#mowerPhoto)" role="img" aria-label="Photo of a red riding mower cutting a green lawn"/>
    </svg>

    <p class="area-band">Serving New Braunfels &amp;<br>Surrounding Areas.</p>

    <h1 class="brand-name">Mr<br>Pellowes<br>Yard<br>Works</h1>

    <section class="offers">
      <div class="offer">
        <div class="offer-title">Lawn Service</div>
        <div class="offer-line">starting at <span class="price"><small>$</small>40</span></div>
        <div class="offer-note">(mowing, edging, leaf blowing)</div>
      </div>
      <div class="offer">
        <div class="offer-title">Tree Trimming</div>
        <div class="offer-line">starting at <span class="price"><small>$</small>125</span></div>
      </div>
    </section>

    <ul class="extras">
      <li>Mulching</li>
      <li>Shrub Trimming</li>
      <li>Aeration</li>
      <li>Flower Bed Maintenance</li>
      <li>Fall/Spring Clean Up</li>
    </ul>

    <section class="contact-zone">
      <div class="contact">
        <p class="lead">To set up and estimates</p>
        <p><b>Call:</b> 512 555 0143</p>
        <p><b>Email:</b> mrpellowesyard@example-mail.net</p>
      </div>
    </section>

    <svg class="service-strip" viewBox="0 0 800 185">
      <defs>
        <linearGradient id="grassFade" x1="0" y1="0" x2="0" y2="1">
          <stop offset="0" stop-color="#e7e7e7"/>
          <stop offset=".35" stop-color="#7cbf3a"/>
          <stop offset="1" stop-color="#2f7d1f"/>
        </linearGradient>
        <linearGradient id="thumbTone" x1="0" y1="0" x2="1" y2="1">
          <stop offset="0" stop-color="#5ea33a"/>
          <stop offset="1" stop-color="#2d6e24"/>
        </linearGradient>
      </defs>
      <rect x="0" y="0" width="800" height="185" fill="url(#grassFade)" role="img" aria-label="Grass border"/>
      <g stroke="var(--white)" stroke-width="4" fill="url(#thumbTone)">
        <circle cx="80" cy="112" r="58" role="img" aria-label="Photo of a push mower on grass"/>
        <circle cx="195" cy="102" r="58" role="img" aria-label="Photo of leaf blowing"/>
        <circle cx="310" cy="92" r="58" role="img" aria-label="Photo of tree trimming"/>
        <circle cx="425" cy="84" r="58" role="img" aria-label="Photo of edging along a walkway"/>
        <circle cx="540" cy="76" r="58" role="img" aria-label="Photo of hedge trimming"/>
        <circle cx="655" cy="68" r="58" role="img" aria-label="Photo of shrub trimming"/>
        <circle cx="770" cy="60" r="58" role="img" aria-label="Photo of a trimmed hedge"/>
      </g>
    </svg>
  </main>
</body>
</html>
```